Professional Word template for reports and concepts

I need a Word template for reports, concepts, guidelines, and lead magnets:
- Cover page
- Table of contents
- Text with various formatting templates for notes, reminders, quotes, visualizations
- Headers and footers
- etc.
The uploaded documents contain a detailed briefing document with all requirements.
Our website is www.varnelpunkt.de
Industry/Entity Type
Profesional Services
Font styles to use
Other font styles liked:
- Open Sans
Look and feel
Each slider illustrates characteristics of the customer's brand and the style your logo design should communicate.

```html
<!DOCTYPE html>
<html lang="en">
<head>
<meta charset="utf-8">
<title>Varnel Punkt – Report Template</title>
<link href="https://fonts.googleapis.com/css2?family=Open+Sans:wght@400;600;700;800&family=Oswald:wght@500;600&display=swap" rel="stylesheet">
<style>
:root{
  --navy:#24528c;
  --blue:#1f6fc0;
  --orange:#f6a31b;
  --light:#dce9f6;
  --ink:#333;
  --muted:#666;
  --stage:#8d8d8d;
}
*{box-sizing:border-box;margin:0;padding:0}
html,body{width:1200px;height:1200px;overflow:hidden}
body{background:radial-gradient(circle at 50% 50%,#a3a3a3,var(--stage));font-family:"Open Sans",sans-serif;color:var(--ink);position:relative}
.page{position:absolute;width:261px;height:368px;background:#fff;overflow:hidden;box-shadow:0 3px 10px rgba(0,0,0,.35)}
.c1{left:30px}.c2{left:324px}.c3{left:618px}.c4{left:912px}
.r1{top:28px}.r2{top:416px}.r3{top:806px}
.abs{position:absolute}
.brand{position:absolute;font-weight:800;font-size:22px;color:var(--navy);letter-spacing:-.5px;line-height:1}
.badge{position:absolute;width:42px;height:40px;border-radius:4px;background:var(--blue)}
.badge::before{content:"";position:absolute;left:0;top:0;right:0;height:18px;background:#fff;border:1px solid #cfd8e3;border-radius:4px 4px 0 0}
.cover-title{position:absolute;font-family:"Oswald",sans-serif;font-weight:600;font-size:17px;line-height:22px;text-transform:uppercase}
.cover-sub{position:absolute;font-size:5.6px;line-height:8px;width:150px}
.contact{position:absolute;font-size:3.6px;line-height:5px}
/* headers */
.hd-left{position:absolute;left:20px;top:18px;font-size:8.5px;color:var(--blue);display:flex;align-items:center;gap:2px;text-transform:uppercase}
.dot{display:inline-block;width:3.5px;height:3.5px;border-radius:50%;background:var(--navy)}
.dot.o{background:var(--orange)}.dot.s{width:2.5px;height:2.5px}
.hd-center{position:absolute;left:24px;right:24px;top:26px;text-align:center;font-size:9.5px;color:#222;text-transform:uppercase;border-bottom:.6px solid #ccc;border-top:.6px solid #e3e3e3;padding:3px 0}
.hd-blue{position:absolute;left:0;right:0;top:18px;text-align:center;font-size:9.5px;color:var(--navy);text-transform:uppercase}
.dotrow{position:absolute;left:0;right:0;top:34px;display:flex;justify-content:center;gap:3px;align-items:center}
/* stripes */
.stripe-r{position:absolute;right:0;top:0;bottom:0;width:11px;background:var(--navy);border-left:4px solid var(--orange)}
.stripe-l{position:absolute;left:0;top:0;bottom:0;width:9px;background:var(--navy)}
.mark{position:absolute;right:22px;bottom:14px;font-weight:800;font-size:32px;color:rgba(36,82,140,.16);line-height:1}
/* toc */
.toc{position:absolute;left:25px;width:208px;top:52px}
.toc h3{font-size:7px;font-weight:600;margin-bottom:6px}
.toc li{list-style:none;display:flex;font-size:4px;line-height:8.6px;color:#444}
.toc li span.l{flex:1;border-bottom:.5px dotted #999;margin:0 4px 3px}
/* text */
.txt{position:absolute;left:28px;width:208px;font-size:3.6px;line-height:4.9px;color:#555}
.txt p{margin-bottom:6px}
.txt h4{font-size:4.4px;font-weight:400;color:#888;margin:4px 0 5px}
.sig{width:40px;height:14px;background:#e7e7e7;margin:4px 0 5px}
.sig-note{width:75px}
/* budget */
.bud{position:absolute;left:27px;width:210px}
.bud h3{font-size:7px;font-weight:700;color:#222;margin:0 0 2px}
.bud p{font-size:3.6px;line-height:4.8px;color:#555;margin-bottom:6px}
table{width:100%;border-collapse:separate;border-spacing:0 1.1px;font-size:3.5px;margin-bottom:8px}
td,th{height:7.5px;padding:0 4px;font-weight:400}
th{background:var(--navy);color:#fff;font-weight:600}
td{background:#eef3f9}
td.n,th.n{text-align:center;width:18%}
tr.ph td{background:var(--light);color:var(--blue)}
tr.tot td{background:#e2e2e2}
tr.grand td{background:var(--blue);color:#fff;font-weight:600}
.orangeset tr.ph2 td{background:var(--orange);color:#fff}
.orangeset th.alt{background:var(--orange)}
/* footers */
.ft2{position:absolute;left:8px;right:12px;bottom:7px;display:flex;align-items:center;gap:2px;font-size:3px;color:#777}
.ft2 .nm{font-weight:800;font-size:5.5px;color:var(--navy);margin-right:2px}
.ft2 .ln{flex:1;height:.5px;background:#bbb;margin:0 4px}
.pg{width:8px;height:8px;border-radius:50%;background:var(--navy);color:#fff;font-size:4px;display:flex;align-items:center;justify-content:center}
.ft3{position:absolute;left:0;right:0;bottom:4px;height:5px;background:var(--navy);display:flex;align-items:center;font-size:2.8px;color:#fff;padding-left:18px;letter-spacing:.6px}
.ft3 b{margin-left:auto;width:16px;height:100%;background:var(--orange);color:#222;font-weight:400;text-align:center;line-height:5px}
/* covers 2 & 3 */
.band-o{position:absolute;left:0;right:0;top:152px;height:12px;background:var(--orange)}
.band-n{position:absolute;left:0;right:0;top:164px;height:146px;background:var(--navy)}
.band-l{position:absolute;left:0;right:0;top:310px;height:3px;background:var(--blue)}
.contacts{position:absolute;left:36px;right:20px;top:342px;display:flex;gap:14px;font-size:3.6px;color:#444;align-items:center}
.contacts span{display:flex;align-items:center;gap:3px}
.ico{width:11px;height:11px;border-radius:50%;background:var(--blue);display:inline-flex;align-items:center;justify-content:center}
</style>
</head>
<body>

<!-- ============ ROW 1 ============ -->
<section class="page c1 r1">
  <svg class="abs" width="261" height="368" viewBox="0 0 261 368" aria-hidden="true">
    <polygon points="178,0 261,0 261,92" fill="#f6a31b"/>
    <polygon points="214,0 261,0 261,54" fill="#24528c"/>
    <polygon points="0,148 0,368 128,368" fill="#f6a31b"/>
    <polygon points="0,196 0,368 104,368" fill="#24528c"/>
  </svg>
  <div class="brand" style="left:74px;top:74px">varnel</div>
  <div class="badge" style="left:142px;top:60px"></div>
  <h1 class="cover-title" style="left:68px;top:128px;color:var(--navy)">Lorem ipsum<br>dolor sit consec</h1>
  <p class="cover-sub" style="left:68px;top:178px">Lorem ipsum dolor sit amet, consectetuer adipiscing elit, sed diam nonummy nibh euÂ ismod tincidunt ut</p>
  <p class="contact" style="left:11px;top:333px;color:#fff">P: +00 40 5550 182<br>E: info@varnelpunkt.de<br>W: www.varnelpunkt.de</p>
</section>

<section class="page c2 r1">
  <div class="hd-left"><i class="dot"></i><i class="dot"></i><i class="dot o s"></i>&nbsp;Table of Contents</div>
  <div class="stripe-r"></div>
  <nav class="toc" style="top:52px">
    <h3>Contents</h3>
    <ul>
      <li>Table of Contents<span class="l"></span>01</li>
      <li>Executive Summary<span class="l"></span>02</li>
      <li>Our Understanding of Your Needs<span class="l"></span>02</li>
      <li>Our Recommendations<span class="l"></span>03</li>
      <li>Our Approach<span class="l"></span>05</li>
      <li>Budget and Timeframe<span class="l"></span>07</li>
      <li>Appendix A: About Harlow Point<span class="l"></span>10</li>
      <li>Appendix B: Selected Client List<span class="l"></span>10</li>
      <li>Appendix C: Our Capabilities<span class="l"></span>11</li>
      <li>Appendix D: Our Process<span class="l"></span>12</li>
    </ul>
  </nav>
  <div class="mark">varnel</div>
</section>

<section class="page c3 r1">
  <div class="stripe-l" style="width:0"></div>
  <div class="hd-left"><i class="dot"></i><i class="dot"></i><i class="dot o s"></i>&nbsp;Executive Summary</div>
  <div class="stripe-r"></div>
  <div class="txt" style="top:40px">
    <p>Lorem ipsum dolor sit amet, consectetuer adipiscing elit, sed diam nonummy nibh euismod tincidunt ut laoreet dolore magna aliquam erat volutpat. Ut wisi enim ad minim veniam, quis nostrud exerci tation ullamcorper suscipit lobortis nisl ut aliquip ex ea commodo consequat. Duis autem vel eum iriure dolor in hendrerit.</p>
    <h4>What We're Proposing</h4>
    <p>Lorem ipsum dolor sit amet, consectetuer adipiscing elit, sed diam nonummy nibh euismod tincidunt ut laoreet dolore magna aliquam erat volutpat. Ut wisi enim ad minim veniam, quis nostrud exerci tation ullamcorper suscipit lobortis nisl ut aliquip ex ea commodo consequat. Duis autem vel eum iriure dolor in hendrerit.</p>
    <h4>What is in Our Proposal</h4>
    <p>Lorem ipsum dolor sit amet, consectetuer adipiscing elit, sed diam nonummy nibh euismod tincidunt ut laoreet dolore magna aliquam erat volutpat. Ut wisi enim ad minim veniam, quis nostrud exerci tation ullamcorper suscipit lobortis nisl ut aliquip ex ea commodo consequat. Duis autem vel eum iriure dolor in hendrerit.</p>
    <p>Lorem ipsum dolor sit amet, consectetuer adipiscing elit, sed diam nonummy nibh euismod tincidunt ut laoreet dolore magna aliquam erat volutpat. Ut wisi enim ad minim veniam, quis nostrud exerci tation ullamcorper.</p>
    <div class="sig" role="img" aria-label="Handwritten signature"></div>
    <p class="sig-note">Lorem ipsum dolor sit amet, consectetuer adipiscing elit, sed diam nonummy nibh euismod tincidunt ut laoreet dolore magna aliquam erat volutpat. Ut</p>
  </div>
  <div class="mark">varnel</div>
</section>

<section class="page c4 r1">
  <div class="stripe-l"></div>
  <div class="hd-left"><i class="dot"></i><i class="dot"></i><i class="dot o s"></i>&nbsp;Budget and Timeframe</div>
  <div class="stripe-r"></div>
  <div class="bud" style="top:44px">
    <h3>Implementation Estimate</h3>
    <p>The bulk of the implementation costs will be defined by discovery. Based on similar CRM implementation projects, we feel expect that the CRM side will be somewhere between 200 and 300 hours, give or take. The wide swing in hours in phase one is related to the ill-defined nature of both the integration needs and our role in the integration project. Our focus in discovery will be to nail down those requirements as it relates to what is needed to integrate the sites with the CRM.</p>
    <table>
      <tr><th>Task</th><th class="n">Hours</th><th class="n">Cost</th></tr>
      <tr><td>Discovery</td><td class="n">40</td><td class="n">$8,000</td></tr>
      <tr class="ph"><td colspan="3">Phase 1</td></tr>
      <tr><td>Discovery</td><td class="n">20-40</td><td class="n">$8,000</td></tr>
      <tr><td>Discovery</td><td class="n">20-40</td><td class="n">$8,000</td></tr>
      <tr><td>Discovery</td><td class="n">20-40</td><td class="n">$8,000</td></tr>
      <tr class="tot"><td>Total Phase 1</td><td class="n">80-240</td><td class="n">$16,800-48,000</td></tr>
      <tr class="ph"><td colspan="3">Phase 2</td></tr>
      <tr><td>Discovery</td><td class="n">20-40</td><td class="n">$8,000</td></tr>
      <tr class="tot"><td>Total Phase 2</td><td class="n">80-240</td><td class="n">$16,800-48,000</td></tr>
      <tr class="grand"><td>Total Estimated Implementation Cost</td><td class="n">220-480</td><td class="n">$44,000-96,000</td></tr>
    </table>
    <h3>Project Timeline</h3>
    <p>Based on the information we have at our disposal, the March launch date doesn't seem a realistic goal to get both the work done needed to provide the foundation for the future CRM instance and the integration given the state of flux of the requirements. That said, we feel it prudent to proceed with discovery before committing. We are currently estimating that the first phase will take somewhere between 7 and 12 weeks.</p>
    <table>
      <tr><th>Task</th><th class="n" style="width:36%">Weeks to Complete</th></tr>
      <tr><td>Discovery</td><td class="n">1-2</td></tr>
      <tr><td>Phase 1</td><td class="n">6-10</td></tr>
      <tr><td>Phase 2</td><td class="n">8-12</td></tr>
      <tr class="tot"><td>Total Number of Weeks</td><td class="n"></td></tr>
    </table>
  </div>
  <div class="mark">varnel</div>
</section>

<!-- ============ ROW 2 ============ -->
<section class="page c1 r2">
  <div class="brand" style="left:62px;top:92px">varnel</div>
  <div class="badge" style="left:146px;top:74px;width:54px;height:54px"></div>
  <div class="band-o"></div><div class="band-n"></div><div class="band-l"></div>
  <h1 class="cover-title" style="left:32px;top:196px;color:#fff">Lorem ipsum<br>dolor sit consec</h1>
  <p class="cover-sub" style="left:32px;top:258px;color:#fff">Lorem ipsum dolor sit amet, consectetuer adipiscing elit, sed diam nonummy nibh euÂ ismod tincidunt ut</p>
  <div class="contacts">
    <span><i class="ico"></i>+00 40 5550 182</span>
    <span><i class="ico"></i>info@varnelpunkt.de</span>
    <span><i class="ico"></i>www.varnelpunkt.de</span>
  </div>
</section>

<section class="page c2 r2">
  <div class="hd-center">Table of Contents</div>
  <nav class="toc" style="top:58px">
    <h3>Contents</h3>
    <ul>
      <li>Table of Contents<span class="l"></span>01</li>
      <li>Executive Summary<span class="l"></span>02</li>
      <li>Our Understanding of Your Needs<span class="l"></span>02</li>
      <li>Our Recommendations<span class="l"></span>03</li>
      <li>Our Approach<span class="l"></span>05</li>
      <li>Budget and Timeframe<span class="l"></span>07</li>
      <li>Appendix A: About Harlow Point<span class="l"></span>10</li>
      <li>Appendix B: Selected Client List<span class="l"></span>10</li>
      <li>Appendix C: Our Capabilities<span class="l"></span>11</li>
      <li>Appendix D: Our Process<span class="l"></span>12</li>
    </ul>
  </nav>
  <footer class="ft2"><span class="nm">varnel</span><i class="dot"></i><i class="dot"></i><i class="dot"></i><i class="dot o s"></i>&nbsp;VARNEL PUNKT<span class="ln"></span><span class="pg">2</span></footer>
</section>

<section class="page c3 r2">
  <div class="hd-center">Executive Summery</div>
  <div class="txt" style="top:48px">
    <p>Lorem ipsum dolor sit amet, consectetuer adipiscing elit, sed diam nonummy nibh euismod tincidunt ut laoreet dolore magna aliquam erat volutpat. Ut wisi enim ad minim veniam, quis nostrud exerci tation ullamcorper suscipit lobortis nisl ut aliquip ex ea commodo consequat. Duis autem vel eum iriure dolor in hendrerit.</p>
    <h4>What We're Proposing</h4>
    <p>Lorem ipsum dolor sit amet, consectetuer adipiscing elit, sed diam nonummy nibh euismod tincidunt ut laoreet dolore magna aliquam erat volutpat. Ut wisi enim ad minim veniam, quis nostrud exerci tation ullamcorper suscipit lobortis nisl ut aliquip ex ea commodo consequat. Duis autem vel eum iriure dolor in hendrerit.</p>
    <h4>What is in Our Proposal</h4>
    <p>Lorem ipsum dolor sit amet, consectetuer adipiscing elit, sed diam nonummy nibh euismod tincidunt ut laoreet dolore magna aliquam erat volutpat. Ut wisi enim ad minim veniam, quis nostrud exerci tation ullamcorper suscipit lobortis nisl ut aliquip ex ea commodo consequat. Duis autem vel eum iriure dolor in hendrerit.</p>
    <p>Lorem ipsum dolor sit amet, consectetuer adipiscing elit, sed diam nonummy nibh euismod tincidunt ut laoreet dolore magna aliquam erat volutpat. Ut wisi enim ad minim veniam, quis nostrud exerci tation ullamcorper.</p>
    <div class="sig" role="img" aria-label="Handwritten signature"></div>
    <p class="sig-note">Lorem ipsum dolor sit amet, consectetuer adipiscing elit, sed diam nonummy nibh euismod tincidunt ut laoreet dolore magna aliquam erat volutpat. Ut</p>
  </div>
  <footer class="ft2"><span class="nm">varnel</span><i class="dot"></i><i class="dot"></i><i class="dot"></i><i class="dot o s"></i>&nbsp;VARNEL PUNKT<span class="ln"></span><span class="pg">2</span></footer>
</section>

<section class="page c4 r2">
  <div class="hd-center">Budget and Timeframe</div>
  <div class="bud orangeset" style="top:44px">
    <h3>Implementation Estimate</h3>
    <p>The bulk of the implementation costs will be defined by discovery. Based on similar CRM implementation projects, we feel expect that the CRM side will be somewhere between 200 and 300 hours, give or take. The wide swing in hours in phase one is related to the ill-defined nature of both the integration needs and our role in the integration project. Our focus in discovery will be to nail down those requirements.</p>
    <table>
      <tr><th>Task</th><th class="n">Hours</th><th class="n">Cost</th></tr>
      <tr><td>Discovery</td><td class="n">40</td><td class="n">$8,000</td></tr>
      <tr class="ph"><td colspan="3">Phase 1</td></tr>
      <tr><td>Discovery</td><td class="n">20-40</td><td class="n">$8,000</td></tr>
      <tr><td>Discovery</td><td class="n">20-40</td><td class="n">$8,000</td></tr>
      <tr><td>Discovery</td><td class="n">20-40</td><td class="n">$8,000</td></tr>
      <tr class="tot"><td>Total Phase 1</td><td class="n">80-240</td><td class="n">$16,800-48,000</td></tr>
      <tr class="ph2"><td colspan="3">Phase 2</td></tr>
      <tr><td>Discovery</td><td class="n">20-40</td><td class="n">$8,000</td></tr>
      <tr class="tot"><td>Total Phase 2</td><td class="n">80-240</td><td class="n">$16,800-48,000</td></tr>
      <tr class="grand"><td>Total Estimated Implementation Cost</td><td class="n">220-480</td><td class="n">$44,000-96,000</td></tr>
    </table>
    <h3>Project Timeline</h3>
    <p>Based on the information we have at our disposal, the March launch date doesn't seem a realistic goal to get both the work done needed to provide the foundation for the future CRM instance and the integration given the state of flux of the requirements. We are currently estimating that the first phase will take somewhere between 7 and 12 weeks.</p>
    <table>
      <tr><th class="alt">Task</th><th class="n alt" style="width:36%">Weeks to Complete</th></tr>
      <tr><td>Discovery</td><td class="n">1-2</td></tr>
      <tr><td>Phase 1</td><td class="n">6-10</td></tr>
      <tr><td>Phase 2</td><td class="n">8-12</td></tr>
      <tr class="grand"><td>Total Number of Weeks</td><td class="n"></td></tr>
    </table>
  </div>
  <footer class="ft2"><span class="nm">varnel</span><i class="dot"></i><i class="dot"></i><i class="dot"></i><i class="dot o s"></i>&nbsp;VARNEL PUNKT<span class="ln"></span><span class="pg">2</span></footer>
</section>

<!-- ============ ROW 3 ============ -->
<section class="page c1 r3">
  <div class="brand" style="left:62px;top:92px">varnel</div>
  <div class="badge" style="left:146px;top:74px;width:54px;height:54px"></div>
  <div class="band-o"></div><div class="band-n"></div><div class="band-l"></div>
  <h1 class="cover-title" style="left:32px;top:196px;color:#fff">Lorem ipsum<br>dolor sit consec</h1>
  <p class="cover-sub" style="left:32px;top:258px;color:#fff">Lorem ipsum dolor sit amet, consectetuer adipiscing elit, sed diam nonummy nibh euÂ ismod tincidunt ut</p>
  <div class="contacts">
    <span><i class="ico"></i>+00 40 5550 182</span>
    <span><i class="ico"></i>info@varnelpunkt.de</span>
    <span><i class="ico"></i>www.varnelpunkt.de</span>
  </div>
</section>

<section class="page c2 r3">
  <div class="hd-blue">Table of Contents</div>
  <div class="dotrow"><i class="dot o s"></i><i class="dot"></i><i class="dot"></i><i class="dot"></i><i class="dot o"></i><i class="dot"></i><i class="dot"></i><i class="dot"></i><i class="dot o s"></i></div>
  <nav class="toc" style="top:56px">
    <h3>Contents</h3>
    <ul>
      <li>Table of Contents<span class="l"></span>01</li>
      <li>Executive Summary<span class="l"></span>02</li>
      <li>Our Understanding of Your Needs<span class="l"></span>02</li>
      <li>Our Recommendations<span class="l"></span>03</li>
      <li>Our Approach<span class="l"></span>05</li>
      <li>Budget and Timeframe<span class="l"></span>07</li>
      <li>Appendix A: About Harlow Point<span class="l"></span>10</li>
      <li>Appendix B: Selected Client List<span class="l"></span>10</li>
      <li>Appendix C: Our Capabilities<span class="l"></span>11</li>
      <li>Appendix D: Our Process<span class="l"></span>12</li>
    </ul>
  </nav>
  <div class="mark" style="bottom:16px">varnel</div>
  <footer class="ft3">VARNEL PUNKT<b>1</b></footer>
</section>

<section class="page c3 r3">
  <div class="hd-blue" style="color:#222">Executive Summery</div>
  <div class="dotrow"><i class="dot o s"></i><i class="dot"></i><i class="dot"></i><i class="dot"></i><i class="dot o"></i><i class="dot"></i><i class="dot"></i><i class="dot"></i><i class="dot o s"></i></div>
  <div class="txt" style="top:50px">
    <p>Lorem ipsum dolor sit amet, consectetuer adipiscing elit, sed diam nonummy nibh euismod tincidunt ut laoreet dolore magna aliquam erat volutpat. Ut wisi enim ad minim veniam, quis nostrud exerci tation ullamcorper suscipit lobortis nisl ut aliquip ex ea commodo consequat. Duis autem vel eum iriure dolor in hendrerit.</p>
    <h4>What We're Proposing</h4>
    <p>Lorem ipsum dolor sit amet, consectetuer adipiscing elit, sed diam nonummy nibh euismod tincidunt ut laoreet dolore magna aliquam erat volutpat. Ut wisi enim ad minim veniam, quis nostrud exerci tation ullamcorper suscipit lobortis nisl ut aliquip ex ea commodo consequat. Duis autem vel eum iriure dolor in hendrerit.</p>
    <h4>What is in Our Proposal</h4>
    <p>Lorem ipsum dolor sit amet, consectetuer adipiscing elit, sed diam nonummy nibh euismod tincidunt ut laoreet dolore magna aliquam erat volutpat. Ut wisi enim ad minim veniam, quis nostrud exerci tation ullamcorper suscipit lobortis nisl ut aliquip ex ea commodo consequat. Duis autem vel eum iriure dolor in hendrerit.</p>
    <p>Lorem ipsum dolor sit amet, consectetuer adipiscing elit, sed diam nonummy nibh euismod tincidunt ut laoreet dolore magna aliquam erat volutpat. Ut wisi enim ad minim veniam, quis nostrud exerci tation ullamcorper.</p>
    <div class="sig" role="img" aria-label="Handwritten signature"></div>
    <p class="sig-note">Lorem ipsum dolor sit amet, consectetuer adipiscing elit, sed diam nonummy nibh euismod tincidunt ut laoreet dolore magna aliquam erat volutpat. Ut</p>
  </div>
  <div class="mark" style="bottom:16px">varnel</div>
  <footer class="ft3">VARNEL PUNKT<b>2</b></footer>
</section>

<section class="page c4 r3">
  <div class="hd-blue" style="color:#222">Budget and Timeframe</div>
  <div class="dotrow"><i class="dot o s"></i><i class="dot"></i><i class="dot"></i><i class="dot"></i><i class="dot o"></i><i class="dot"></i><i class="dot"></i><i class="dot"></i><i class="dot o s"></i></div>
  <div class="bud" style="top:44px">
    <h3>Implementation Estimate</h3>
    <p>The bulk of the implementation costs will be defined by discovery. Based on similar CRM implementation projects, we feel expect that the CRM side will be somewhere between 200 and 300 hours, give or take. The wide swing in hours in phase one is related to the ill-defined nature of both the integration needs and our role in the integration project. Our focus in discovery will be to nail down those requirements.</p>
    <table>
      <tr><th>Task</th><th class="n">Hours</th><th class="n">Cost</th></tr>
      <tr><td>Discovery</td><td class="n">40</td><td class="n">$8,000</td></tr>
      <tr class="ph"><td colspan="3">Phase 1</td></tr>
      <tr><td>Discovery</td><td class="n">20-40</td><td class="n">$8,000</td></tr>
      <tr><td>Discovery</td><td class="n">20-40</td><td class="n">$8,000</td></tr>
      <tr><td>Discovery</td><td class="n">20-40</td><td class="n">$8,000</td></tr>
      <tr class="tot"><td>Total Phase 1</td><td class="n">80-240</td><td class="n">$16,800-48,000</td></tr>
      <tr class="ph"><td colspan="3">Phase 2</td></tr>
      <tr><td>Discovery</td><td class="n">20-40</td><td class="n">$8,000</td></tr>
      <tr class="tot"><td>Total Phase 2</td><td class="n">80-240</td><td class="n">$16,800-48,000</td></tr>
      <tr class="grand"><td>Total Estimated Implementation Cost</td><td class="n">220-480</td><td class="n">$44,000-96,000</td></tr>
    </table>
    <h3>Project Timeline</h3>
    <p>Based on the information we have at our disposal, the March launch date doesn't seem a realistic goal to get both the work done needed to provide the foundation for the future CRM instance and the integration given the state of flux of the requirements. We are currently estimating that the first phase will take somewhere between 7 and 12 weeks.</p>
    <table>
      <tr><th>Task</th><th class="n" style="width:36%">Weeks to Complete</th></tr>
      <tr><td>Discovery</td><td class="n">1-2</td></tr>
      <tr><td>Phase 1</td><td class="n">6-10</td></tr>
      <tr><td>Phase 2</td><td class="n">8-12</td></tr>
      <tr class="tot"><td>Total Number of Weeks</td><td class="n"></td></tr>
    </table>
  </div>
  <div class="mark" style="bottom:16px">varnel</div>
  <footer class="ft3">VARNEL PUNKT<b>3</b></footer>
</section>

</body>
</html>
```